Homepage/Landing Page for Kelvadu.com

We need a brochure style landing page for our website, kelvadu.com. The new homepage will direct people either to trademarkhub.com (a website for businesses to purchase printing), to a landing page about trading cards/sports memorabilia, or to a website about high-end embellished cartons/boxes.
The existing site, www.kelvadu.com, will become trademarkhub.com, and people arriving at kelvadu.com will be shown three options to choose based on their needs:
1) Business Printing - for everyone from micro-businesses on up, our manufacturing process insures we have something to suit every business.
2) Highly decorated and embellished cartons - perfect for new brands, prototypes, pilot programs, seasonal packaging
3) Trading cards/sports memorabilia - Handling cards for athletes from Tidy Circuit to high school, college and beyond.

Target Market(s)

Target market is small business owners and print buyers

Industry/Entity Type

Printing and Packaging

Number of Pages Required

1 page

Font styles to use
Other font styles liked:
• See the KV Web Flip Standards PDF attached.

Requirements
Must have
• 3 clearly marked paths for customers to follow - use web standards pdf below for fonts and colors
Should not have
• My project should not feel trendy or faddish, but modern and professional.

```html
<!DOCTYPE html>
<html lang="en">
<head>
<meta charset="utf-8">
<title>Kelvadu — Positively Different</title>
<link href="https://fonts.googleapis.com/css2?family=Domine:wght@400;700&family=Poppins:wght@400;500;600&display=swap" rel="stylesheet">
<style>
:root{
  --teal:#0aa7c4;
  --teal-tint:#bfe6ee;
  --ink:#161616;
  --body:#3a3a3a;
  --pale:#d8eaf0;
  --sky:#67b3cb;
  --band:#f2f2f2;
  --foot:#000;
  --white:#fff;
}
*{margin:0;padding:0;box-sizing:border-box}
html,body{width:1200px;height:2881px;overflow:hidden;background:var(--white)}
body{position:relative;font-family:"Poppins",sans-serif;color:var(--ink)}
.abs{position:absolute}
.serif{font-family:"Domine",serif}

/* header */
.brand{left:88px;top:98px;font-size:17px;font-weight:600;color:var(--ink);letter-spacing:-.3px}
.nav{left:222px;top:32px;display:flex;gap:24px;font-size:14.5px;font-weight:500}
.call{left:741px;top:26px;display:flex;gap:12px;align-items:center;font-size:14px;font-weight:500;line-height:1.25}
.login{left:915px;top:33px;font-size:14.5px;font-weight:500}
.register{left:966px;top:21px;width:113px;height:42px;border:2px solid var(--teal);display:flex;align-items:center;justify-content:center;font-size:14.5px;font-weight:500}
.search{left:1093px;top:32px}

/* hero */
.hero-photo{left:522px;top:86px;width:678px;height:638px;background:linear-gradient(135deg,#e9eef0 0%,#cfd8dc 40%,#c58ac9 60%,#d9a34a 85%)}
.accent{background:var(--teal-tint)}
.accent-tall{left:476px;top:531px;width:46px;height:248px}
.accent-base{left:522px;top:724px;width:76px;height:55px}
.eyebrow{left:88px;top:368px;font-size:29px;color:var(--teal)}
.headline{left:88px;top:405px;font-size:77px;line-height:80px;font-weight:700;color:var(--ink)}

/* needs */
.needs-title{left:0;width:1200px;top:852px;text-align:center;font-size:38px;line-height:39px;font-weight:700}
.card{top:950px;width:276px;height:302px;background:var(--white);box-shadow:0 14px 30px rgba(10,167,196,.18);text-align:center}
.card svg{margin-top:45px}
.card p{position:absolute;left:20px;right:20px;top:154px;font-size:14.6px;line-height:19.6px;color:var(--body)}

/* promos */
.promo-left{left:0;top:1383px;width:600px;height:509px;background:var(--pale)}
.promo-left .shot{position:absolute;left:0;bottom:0;width:600px;height:190px;background:linear-gradient(160deg,#c9c2a8,#9a9a9a 50%,#e9e9e4)}
.promo-name{position:absolute;left:0;width:600px;top:104px;text-align:center;font-family:"Domine",serif;font-size:40px;color:#1f8a96}
.promo-copy{position:absolute;left:140px;width:320px;top:201px;text-align:center;font-size:15px;line-height:19.6px;color:var(--body)}
.more{font-size:14px;font-weight:600;letter-spacing:.5px}
.promo-left .more{position:absolute;left:242px;top:273px;color:var(--teal)}
.promo-right{left:600px;top:1383px;width:600px;height:509px;background:linear-gradient(160deg,#5aa9c3 0%,var(--sky) 55%,#7bbdd2 100%)}
.promo-right .name{position:absolute;left:63px;top:228px;font-size:50px;color:var(--white);font-weight:400}
.promo-right p{position:absolute;left:63px;top:293px;width:290px;font-size:15px;line-height:19.6px;color:var(--white)}
.promo-right .more{position:absolute;left:61px;top:340px;color:var(--white)}

/* exclusive band */
.exclusive{left:0;top:1892px;width:1200px;height:223px;background:var(--band)}
.exclusive h2{position:absolute;left:202px;top:70px;font-family:"Domine",serif;font-size:37px;line-height:40px;font-weight:700}
.exclusive p{position:absolute;left:203px;top:162px;font-size:15px;color:var(--body)}
.exclusive .swatch{position:absolute;left:727px;top:40px;width:290px;height:183px;background:linear-gradient(125deg,#f3efe6 0%,#f0a450 35%,#0f1b1d 55%,#1d7f80 80%,#0f1b1d 100%);clip-path:polygon(20% 0,45% 0,100% 100%,5% 100%)}

/* community */
.community{left:0;width:1200px;top:2228px;text-align:center}
.community h2{font-family:"Domine",serif;font-size:40px;font-weight:700}
.community p{margin-top:8px;font-size:16px;color:var(--body)}
.invite{left:535px;top:2322px;width:129px;height:42px;background:var(--teal);color:var(--white);font-weight:600;font-size:15px;display:flex;align-items:center;justify-content:center;letter-spacing:.5px}

/* footer */
.footer{left:0;top:2469px;width:1200px;height:412px;background:var(--foot);color:var(--white)}
.foot-brand{position:absolute;left:173px;top:185px;font-size:30px;font-weight:600}
.col{position:absolute;top:128px}
.col h3{font-family:"Domine",serif;font-size:19px;font-weight:700;margin-bottom:6px}
.col li{list-style:none;font-size:13px;line-height:22.3px}
.col.contact li{display:flex;gap:8px;align-items:flex-start}
.col.contact li svg{margin-top:5px;flex:none}
.rule{position:absolute;left:88px;top:353px;width:1024px;height:1px;background:#333}
.copyright{position:absolute;left:0;width:1200px;top:374px;text-align:center;font-family:"Domine",serif;font-size:15px}
.chat{position:absolute;left:1126px;top:320px;width:52px;height:52px;border-radius:50%;background:var(--teal);display:flex;align-items:center;justify-content:center}
</style>
</head>
<body>

<header>
  <div class="abs brand">kelvadu</div>
  <nav class="abs nav"><span>Products</span><span>Services</span><span>About Us</span><span>How to Reach Us</span></nav>
  <div class="abs call">
    <svg width="26" height="26" viewBox="0 0 24 24"><path fill="var(--teal)" d="M6.6 10.8a15.1 15.1 0 0 0 6.6 6.6l2.2-2.2c.3-.3.7-.4 1-.2 1.1.4 2.3.6 3.6.6.6 0 1 .4 1 1V20c0 .6-.4 1-1 1A17 17 0 0 1 3 4c0-.6.4-1 1-1h3.5c.6 0 1 .4 1 1 0 1.3.2 2.5.6 3.6.1.3 0 .7-.2 1z"/></svg>
    <div>Call Us!<br>(800-555-0148)</div>
  </div>
  <div class="abs login">Login</div>
  <div class="abs register">Register</div>
  <svg class="abs search" width="20" height="20" viewBox="0 0 20 20"><circle cx="8" cy="8" r="6" fill="none" stroke="var(--ink)" stroke-width="2"/><line x1="12.5" y1="12.5" x2="18" y2="18" stroke="var(--ink)" stroke-width="2.2"/></svg>
</header>

<section>
  <div class="abs accent accent-tall" role="img" aria-label="Decorative teal accent"></div>
  <div class="abs accent accent-base" role="img" aria-label="Decorative teal accent"></div>
  <div class="abs hero-photo" role="img" aria-label="Photo of two women working together at a printer in a bright office"></div>
  <div class="abs eyebrow serif">kelvadu</div>
  <h1 class="abs headline serif">Positively<br>Different.</h1>
</section>

<section>
  <h2 class="abs needs-title serif">Choose based on<br>their needs</h2>

  <div class="abs card" style="left:173px">
    <svg width="94" height="84" viewBox="0 0 94 84" fill="none" stroke="var(--teal)" stroke-width="3">
      <rect x="22" y="2" width="50" height="22"/>
      <rect x="2" y="24" width="90" height="34" rx="3"/>
      <rect x="22" y="42" width="50" height="40" fill="var(--white)"/>
      <line x1="32" y1="54" x2="62" y2="54"/><line x1="32" y1="64" x2="62" y2="64"/><line x1="32" y1="73" x2="52" y2="73"/>
      <line x1="76" y1="34" x2="84" y2="34"/>
    </svg>
    <p>Business Printing - for everyone from micro-businesses on up, our manufacturing process insures we have something to suit every business.</p>
  </div>

  <div class="abs card" style="left:462px">
    <svg width="90" height="84" viewBox="0 0 90 84" fill="none" stroke="var(--teal)" stroke-width="3">
      <path d="M20 82V50a25 25 0 0 1 50 0v32"/>
      <path d="M12 40a33 33 0 0 1 66 0"/>
      <circle cx="32" cy="38" r="11"/><circle cx="58" cy="38" r="11"/>
      <line x1="43" y1="38" x2="47" y2="38"/>
      <path d="M38 82v-10h14v10"/>
    </svg>
    <p>Highly decorated and embellished cartons - perfect for new brands, prototypes, pilot programs, seasonal packaging</p>
  </div>

  <div class="abs card" style="left:749px">
    <svg width="80" height="84" viewBox="0 0 80 84" fill="none" stroke="var(--teal)" stroke-width="3">
      <rect x="4" y="2" width="46" height="64" rx="3"/>
      <rect x="26" y="16" width="50" height="66" rx="3" fill="var(--white)"/>
      <circle cx="51" cy="40" r="9"/>
      <path d="M36 74a15 15 0 0 1 30 0"/>
      <line x1="14" y1="14" x2="14" y2="52"/>
    </svg>
    <p>Trading cards/sports memorabilia - Handling cards for athletes from Tidy Circuit to high school, college and beyond.</p>
  </div>
</section>

<section>
  <div class="abs promo-left">
    <div class="promo-name">ClearProof</div>
    <p class="promo-copy">See the actual product, with all your optional finishes and details,before your project goes to press.</p>
    <span class="more">LEARN MORE</span>
    <div class="shot" role="img" aria-label="Photo of an open printed proposal brochure"></div>
  </div>
  <div class="abs promo-right" role="img" aria-label="Photo of pencils, business cards, envelope and glasses on a blue desk">
    <div class="name">TrueTone</div>
    <p>95% of the Hueline library without the hassle, cost or delay of special mixes.</p>
    <span class="more">LEARN MORE</span>
  </div>
</section>

<section class="abs exclusive">
  <h2>Surprising Different Print<br>Exclusively</h2>
  <p>For the Creative Indusrty</p>
  <div class="swatch" role="img" aria-label="Photo of a colour swatch fan guide"></div>
</section>

<section class="abs community">
  <h2>Grow the community, get great stuff</h2>
  <p>invite your colleagues to gain exclusive tools and resources</p>
</section>
<div class="abs invite">INVITE</div>

<footer class="abs footer">
  <div class="foot-brand">kelvadu</div>
  <div class="col" style="left:361px">
    <h3>Expect More</h3>
    <ul><li>All Products</li><li>TrueTone™</li><li>ClearProof™</li><li>Turnaround</li></ul>
  </div>
  <div class="col" style="left:604px">
    <h3>About Us</h3>
    <ul><li>Creatives Only</li><li>Terms of Service</li><li>Privacy Policy</li><li>FAQ</li><li>Refer a Colleague</li></ul>
  </div>
  <div class="col contact" style="left:826px">
    <h3>Contact Us</h3>
    <ul>
      <li><svg width="12" height="12" viewBox="0 0 24 24"><path fill="var(--teal)" d="M6.6 10.8a15.1 15.1 0 0 0 6.6 6.6l2.2-2.2c.3-.3.7-.4 1-.2 1.1.4 2.3.6 3.6.6.6 0 1 .4 1 1V20c0 .6-.4 1-1 1A17 17 0 0 1 3 4c0-.6.4-1 1-1h3.5c.6 0 1 .4 1 1 0 1.3.2 2.5.6 3.6.1.3 0 .7-.2 1z"/></svg>800.GoKelvadu (800.555.0148)</li>
      <li><svg width="12" height="12" viewBox="0 0 24 24"><path fill="var(--teal)" d="M12 2a7 7 0 0 0-7 7c0 5 7 13 7 13s7-8 7-13a7 7 0 0 0-7-7zm0 9.5A2.5 2.5 0 1 1 12 6.5a2.5 2.5 0 0 1 0 5z"/></svg><span>Kelvadu<br>1180 Larkspur Avenue<br>Brenwick (Denton), TX 75910</span></li>
      <li><svg width="12" height="12" viewBox="0 0 24 24"><path fill="var(--teal)" d="M2 5h20v14H2zm2 2v.5l8 5 8-5V7l-8 5z"/></svg>support@kelvadu.com</li>
    </ul>
  </div>
  <div class="rule"></div>
  <div class="copyright">Copyright ©2022 Kelvadu.com. All Rights Reserved.</div>
  <div class="chat">
    <svg width="26" height="24" viewBox="0 0 26 24"><path fill="var(--white)" d="M13 2C6.4 2 1 6.3 1 11.6c0 2.8 1.5 5.3 3.9 7.1L4 23l4.6-2.6c1.4.4 2.9.6 4.4.6 6.6 0 12-4.3 12-9.4S19.6 2 13 2z"/><circle cx="8" cy="11.6" r="1.6" fill="var(--teal)"/><circle cx="13" cy="11.6" r="1.6" fill="var(--teal)"/><circle cx="18" cy="11.6" r="1.6" fill="var(--teal)"/></svg>
  </div>
</footer>

</body>
</html>
```